Business card for Tolvery Anesthesia LLC

This is for a business care for Tolvery Anesthesia LLC. Dr. Lisbeth Tolvery, CRNA, DNAP is the sole provider in the LLC. Business address is 4718 N Brackley Street,
Oakhaven, PA 17342
CRNA stands for certified registered nurse anesthetist
"Keeping you safe and comfortable"
I plan to give this business card to the patients that I provide anesthesia to.
Creative design that ties into Anesthesia. Calm soothing colors.

Target Market(s)

Business card for my patients.

Industry/Entity Type

Medicine

Contact Information for Business Card

Creative, professional, eye catching

Logo Text

Tolvery Anesthesia

Font styles to use
Serif
Script

Colors

Designer to choose colors to be used in the design.

Requirements
Must have
• Tolvery Anesthesia
• Dr. Lisbeth Tolvery, CRNA, DNAP
• tolvery.anesthesia@ quillmail.net
Nice to have
• "Keeping you safe and comfortable"
Should not have
• phone number

```html
<!DOCTYPE html>
<html lang="en">
<head>
<meta charset="utf-8">
<title>Tolvery Anesthesia LLC — Business Card</title>
<link rel="stylesheet" href="https://fonts.googleapis.com/css2?family=Libre+Baskerville:ital,wght@0,400;0,700;1,400&family=Pinyon+Script&display=swap">
<style>
  :root {
    --page-bg: #f3f3f3;
    --brand-blue: #0aa0e2;
    --brand-blue-deep: #0391d6;
    --brand-blue-light: #5ccaf3;
    --ink-dark: #3a3a3c;
    --rule-grey: #7b7b7e;
    --card-white: #ffffff;
  }
  * { box-sizing: border-box; margin: 0; padding: 0; }
  html, body { width: 1200px; height: 891px; overflow: hidden; }
  body {
    background: var(--page-bg);
    font-family: "Libre Baskerville", Georgia, serif;
    position: relative;
  }
  .brand-lockup {
    position: absolute;
    display: flex;
    align-items: center;
    gap: 12px;
  }
  .brand-lockup__dot {
    border-radius: 50%;
    background: var(--brand-blue);
    flex: none;
  }
  .brand-lockup__name {
    font-weight: 700;
    color: var(--ink-dark);
    letter-spacing: 0.02em;
    white-space: nowrap;
  }
  .page-lockup { left: 66px; top: 62px; }
  .page-lockup .brand-lockup__dot { width: 46px; height: 46px; }
  .page-lockup .brand-lockup__name { font-size: 30px; }

  .corner-lockup { right: 70px; bottom: 86px; }
  .corner-lockup .brand-lockup__dot { width: 42px; height: 42px; background: var(--brand-blue-light); }
  .corner-lockup .brand-lockup__name { font-size: 13px; color: var(--rule-grey); font-weight: 400; }

  .card {
    position: absolute;
    width: 440px;
    height: 252px;
    overflow: hidden;
    box-shadow: 0 6px 18px rgba(0,0,0,0.14);
  }
  .card__art { position: absolute; inset: 0; width: 100%; height: 100%; }

  .card--back { left: 660px; top: 250px; background: var(--brand-blue-deep); }
  .card--back .brand-lockup { left: 50%; top: 78px; transform: translateX(-50%); }
  .card--back .brand-lockup__dot { width: 26px; height: 26px; background: var(--card-white); }
  .card--back .brand-lockup__name { font-size: 17px; color: var(--card-white); }
  .card--back .tagline { left: 0; right: 0; top: 124px; text-align: center; }

  .card--front { left: 190px; top: 470px; background: var(--card-white); }
  .card--front .brand-lockup { left: 34px; top: 32px; }
  .card--front .brand-lockup__dot { width: 28px; height: 28px; }
  .card--front .brand-lockup__name { font-size: 18px; }

  .contact { position: absolute; left: 34px; top: 84px; }
  .contact__name { font-size: 15px; font-weight: 700; color: var(--ink-dark); }
  .contact__credentials {
    font-size: 10px; font-style: italic; color: var(--brand-blue); margin-top: 5px;
  }
  .contact__email {
    display: flex; align-items: center; gap: 6px;
    font-size: 9px; color: var(--ink-dark); margin-top: 12px;
  }
  .contact__email svg { width: 11px; height: 9px; flex: none; }

  .tagline {
    position: absolute;
    font-family: "Pinyon Script", cursive;
    color: var(--card-white);
    font-size: 24px;
    line-height: 1.15;
  }
  .card--front .tagline { left: 262px; top: 168px; }
</style>
</head>
<body>

  <div class="brand-lockup page-lockup">
    <span class="brand-lockup__dot"></span>
    <span class="brand-lockup__name">Tolvery Anesthesia</span>
  </div>

  <section class="card card--back" aria-label="Card back">
    <svg class="card__art" viewBox="0 0 440 252" preserveAspectRatio="none" aria-hidden="true">
      <defs>
        <radialGradient id="backGlow" cx="0.6" cy="0.85" r="0.6">
          <stop offset="0" stop-color="#5ccaf3"/>
          <stop offset="1" stop-color="#0391d6" stop-opacity="0"/>
        </radialGradient>
        <radialGradient id="backGlowTop" cx="0.35" cy="0.25" r="0.45">
          <stop offset="0" stop-color="#4fc3f0" stop-opacity="0.8"/>
          <stop offset="1" stop-color="#0aa0e2" stop-opacity="0"/>
        </radialGradient>
      </defs>
      <rect width="440" height="252" fill="#0aa0e2"/>
      <path d="M0 40 C 90 110, 180 110, 260 70 C 330 40, 400 30, 440 40 L440 0 L0 0Z" fill="#0396da"/>
      <rect width="440" height="252" fill="url(#backGlowTop)"/>
      <path d="M0 170 C 120 190, 210 230, 300 210 C 370 195, 420 170, 440 150 L440 252 L0 252Z" fill="url(#backGlow)"/>
    </svg>
    <div class="brand-lockup">
      <span class="brand-lockup__dot"></span>
      <span class="brand-lockup__name">Tolvery Anesthesia</span>
    </div>
    <p class="tagline">Keeping you safe<br>and comfortable...</p>
  </section>

  <section class="card card--front" aria-label="Card front">
    <svg class="card__art" viewBox="0 0 440 252" preserveAspectRatio="none" aria-hidden="true">
      <defs>
        <linearGradient id="frontBlue" x1="0" y1="0" x2="1" y2="1">
          <stop offset="0" stop-color="#0aa0e2"/>
          <stop offset="0.55" stop-color="#4cc2f1"/>
          <stop offset="1" stop-color="#0391d6"/>
        </linearGradient>
      </defs>
      <path d="M250 252 C 236 200, 250 160, 310 148 L440 120 L440 112 L304 140 C 240 154, 226 200, 240 252Z" fill="var(--rule-grey)"/>
      <path d="M258 252 C 246 204, 262 168, 318 156 L440 130 L440 252Z" fill="url(#frontBlue)"/>
      <path d="M330 252 C 380 220, 400 180, 380 150 C 420 170, 430 210, 420 252Z" fill="#ffffff" opacity="0.12"/>
    </svg>
    <div class="brand-lockup">
      <span class="brand-lockup__dot"></span>
      <span class="brand-lockup__name">Tolvery Anesthesia</span>
    </div>
    <div class="contact">
      <p class="contact__name">Dr. Lisbeth Tolvery,</p>
      <p class="contact__credentials">CRNA, DNAP</p>
      <p class="contact__email">
        <svg viewBox="0 0 11 9" aria-hidden="true"><rect x="0.5" y="0.5" width="10" height="8" fill="none" stroke="#0aa0e2"/><path d="M0.5 0.5 L5.5 5 L10.5 0.5" fill="none" stroke="#0aa0e2"/></svg>
        tolvery.anesthesia@ quillmail.net
      </p>
    </div>
    <p class="tagline">Keeping you safe<br>and comfortable...</p>
  </section>

  <div class="brand-lockup corner-lockup">
    <span class="brand-lockup__dot"></span>
    <span class="brand-lockup__name">Tolvery Anesthesia</span>
  </div>

</body>
</html>
```